Start-up Dog Daycare Needs a Retractable Banner Design for Career Fair

We are a dog daycare located in San Francisco, California, called TailNest Dog Daycare. Our small but dog-knowledgeable team gets to interact with and care for dogs on a daily basis where we supervise playgroups of various sizes. We will like a modern yet fun banner to attract potential new hires and interns. We will like the final design to communicate that we are seeking people who love dogs but who are also hard workers that can thrive in a team setting.

The product specs are as follows:
Document Trim Size - 33.13 X 86.18 inches (84.1 X 218.9cm) with 3312 X 8618 pixels.
Full Bleed Size - 33.38 X 86.43 inches (84.8 X 219.5cm) with 3338 X 8643 pixels.

Additionally, to get a better idea of our brand, attached will be our Company Brand Identity.
Furthermore, attached will be the text we will like included onto our banner.

Target Market(s)

Students at a University

Industry/Entity Type

Pet Care

Font styles to use
Sans Serif

Colors
33a6d7
fbee3e

Requirements
Must have
• Our company logo must be incorporated onto our banner.
• Please include the text in the following order:
• 1. "Dog lovers come talk to us"
• 2. "Internships and full-time positions available"
• Banner Size Specifications:
• Full Bleed Size
• 33.38" x 86.43"
• 84.8 x 219.5 cm
• 3338 x 8643 pixels
• Document Trim Size
• 33.13" x 86.18"
• 84.1 x 218.9 cm
• 3312 x 8618 pixels
• Finished artwork should extend to fill the full bleed area to avoid white edges around.
Nice to have
• - Colors Blue and Yellow
• - Image(s) of a dog(s) playing

```html
<!DOCTYPE html>
<html lang="en">
<head>
<meta charset="utf-8">
<title>TailNest Dog Daycare – Career Fair Banner</title>
<link rel="stylesheet" href="https://fonts.googleapis.com/css2?family=Ubuntu:wght@500;700&display=swap">
<style>
  :root {
    --sky: #85c9e8;
    --mist: #f1f1f1;
    --sun: #fbee3e;
    --brand-blue: #33a6d7;
    --ink: #404040;
    --white: #ffffff;
    --logo-gold: #f2d12f;
    --logo-mark: #e8e3d9;
    --grass-top: #1f3a22;
    --grass-mid: #3f6a2c;
    --grass-bottom: #7fb04a;
    --pup-light: #f0d6a8;
    --pup-dark: #c99a5e;
  }
  * { margin: 0; padding: 0; box-sizing: border-box; }
  html, body {
    width: 1200px;
    height: 3124px;
    overflow: hidden;
    background: var(--sky);
  }
  .banner {
    position: relative;
    width: 1200px;
    height: 3124px;
    overflow: hidden;
    font-family: "Ubuntu", sans-serif;
  }
  .banner-shapes {
    position: absolute;
    inset: 0;
    width: 1200px;
    height: 3124px;
  }
  .logo-tab {
    position: absolute;
    left: 323px;
    top: 0;
    width: 511px;
    height: 338px;
    background: var(--white);
    border-radius: 0 0 42px 42px;
    text-align: center;
  }
  .logo-dot {
    position: absolute;
    left: 205px;
    top: 36px;
    width: 100px;
    height: 100px;
    border-radius: 50%;
    background: var(--logo-mark);
  }
  .logo-name {
    position: absolute;
    left: 0;
    right: 0;
    top: 162px;
    font-size: 74px;
    font-weight: 700;
    line-height: 1;
    color: var(--logo-gold);
  }
  .logo-tagline {
    position: absolute;
    left: 0;
    right: 0;
    top: 258px;
    font-size: 20px;
    font-weight: 700;
    letter-spacing: 3px;
    color: #222;
  }
  .puppy-photo {
    position: absolute;
    left: 866px;
    top: 386px;
    width: 240px;
    height: 365px;
    border-radius: 110px 110px 60px 60px;
    background: linear-gradient(180deg, var(--pup-light), var(--pup-dark));
  }
  .headline {
    position: absolute;
    left: 152px;
    top: 838px;
    font-size: 136px;
    font-weight: 500;
    line-height: 152px;
    color: var(--ink);
    letter-spacing: 1px;
  }
  .headline .accent { color: var(--brand-blue); }
  .openings {
    position: absolute;
    left: 56px;
    top: 2668px;
    font-size: 92px;
    font-weight: 500;
    line-height: 104px;
    color: var(--white);
    -webkit-text-stroke: 1.5px #2a4a5a;
  }
  .openings .accent { color: var(--sun); }
</style>
</head>
<body>
<main class="banner">
  <svg class="banner-shapes" viewBox="0 0 575 1497" preserveAspectRatio="none" aria-hidden="false">
    <defs>
      <linearGradient id="field" x1="0" y1="0" x2="0" y2="1">
        <stop offset="0" stop-color="var(--grass-top)"/>
        <stop offset="0.45" stop-color="var(--grass-mid)"/>
        <stop offset="1" stop-color="var(--grass-bottom)"/>
      </linearGradient>
    </defs>
    <!-- sky background -->
    <rect class="sky" x="0" y="0" width="575" height="1497" fill="var(--sky)"/>
    <!-- upper yellow ribbon -->
    <path class="ribbon-top" d="M0,200 C160,225 330,325 575,332 L575,360 L0,360 Z" fill="var(--sun)"/>
    <!-- photo field area -->
    <path role="img" aria-label="Photo of a terrier running across a green lawn carrying a yellow stick" d="M0,700 L575,590 L575,1260 L0,1260 Z" fill="url(#field)"/>
    <!-- yellow edge under headline panel -->
    <path class="ribbon-mid" d="M0,700 C150,690 350,640 575,592 L575,606 C380,660 190,745 0,755 Z" fill="var(--sun)"/>
    <!-- headline panel -->
    <path class="headline-panel" d="M0,236 C170,258 350,342 575,348 L575,598 C390,640 190,708 0,716 Z" fill="var(--mist)"/>
    <!-- lower yellow ribbon -->
    <path class="ribbon-bottom" d="M0,1098 C150,1140 360,1225 575,1232 L575,1260 L0,1260 Z" fill="var(--sun)"/>
    <!-- blue footer -->
    <path class="footer-panel" d="M0,1112 C150,1155 360,1240 575,1250 L575,1497 L0,1497 Z" fill="var(--brand-blue)"/>
    <!-- divider with loop icon -->
    <g class="divider" stroke="var(--white)" stroke-width="1" fill="none" opacity="0.9">
      <line x1="22" y1="1455" x2="265" y2="1455"/>
      <line x1="310" y1="1455" x2="553" y2="1455"/>
      <circle cx="283" cy="1455" r="5"/>
      <circle cx="293" cy="1455" r="5"/>
    </g>
  </svg>

  <header class="logo-tab">
    <span class="logo-dot"></span>
    <div class="logo-name">TailNest</div>
    <div class="logo-tagline">DOG DAYCARE</div>
  </header>

  <div class="puppy-photo" role="img" aria-label="Photo of a golden retriever puppy sitting"></div>

  <h1 class="headline">DOG LOVERS<br>COME TALK<br><span class="accent">TO US!</span></h1>

  <p class="openings">INTERNSHIPS<br>AND FULL-TIME<br>POSITIONS <span class="accent">AVAILABLE!</span></p>
</main>
</body>
</html>
```